Stationery Design Project

I am a personal trainer in the fitness industry based in Miami. I have recently designed a logo for my company, now i need to market my name through selected stationery designs.
I need an email signature, invoice and a business card. I am looking for a design that is fresh and eye catching to my target audience.
Updates

Reason: Waiting for photo to be taken for business card.

Target Market(s)

25 to 65 years old - male and female - overweight, sedentary and athletic clientele - middle to wealthy economic class

Industry/Entity Type

Personal Trainer

Requirements
Must have
• Will attach Zip file with logo, template of invoice and personal information.
Will attach photo for business card in the next few days.
Nice to have
• Black backdrop logo image for banner of Invoice, with transparent images of my logo.
White backdrop logo image for Email signature, with font that works well with logo.

```html
<!DOCTYPE html>
<html lang="en">
<head>
<meta charset="utf-8">
<title>Pulse Motion Studio – Business Card</title>
<link rel="stylesheet" href="https://fonts.googleapis.com/css2?family=Open+Sans:wght@400;600;700&display=swap">
<style>
  :root {
    --backdrop: #ece6dc;
    --card: #ffffff;
    --card-edge: #d9d4cc;
    --ink: #3a3a3a;
    --brand-orange: #e8571e;
    --orange-deep: #e04e1d;
    --orange-warm: #f08a1c;
    --sun-yellow: #f6c21c;
    --white: #ffffff;
  }
  * { margin: 0; padding: 0; box-sizing: border-box; }
  html, body { width: 1200px; height: 411px; overflow: hidden; }
  body {
    position: relative;
    background: var(--backdrop);
    font-family: "Open Sans", Arial, sans-serif;
    color: var(--ink);
  }
  .card {
    position: absolute;
    top: 57px;
    width: 525px;
    height: 301px;
    background: var(--card);
    border: 1px solid var(--card-edge);
    overflow: hidden;
  }
  .card--front { left: 55px; }
  .card--back { left: 617px; }

  .brand {
    position: absolute;
    text-align: center;
    color: var(--brand-orange);
    font-weight: 700;
    letter-spacing: 1px;
    line-height: 1.05;
  }
  .brand__dot {
    display: block;
    margin: 0 auto 14px;
    width: 58px;
    height: 58px;
    border-radius: 50%;
    background: var(--brand-orange);
  }
  .brand__name { display: block; font-size: 27px; }
  .brand__sub { display: block; font-size: 18px; letter-spacing: 4px; }

  .card--front .brand { left: 32px; width: 270px; top: 40px; }
  .card--back .brand { left: 0; width: 525px; top: 96px; }

  .contact {
    position: absolute;
    left: 0;
    width: 400px;
    top: 186px;
    text-align: center;
    font-size: 12.5px;
    line-height: 21.5px;
    list-style: none;
  }
  .accent-area {
    position: absolute;
    left: 330px;
    top: 190px;
    width: 195px;
    height: 111px;
    border-top-left-radius: 100px;
    background: linear-gradient(90deg, var(--sun-yellow), var(--orange-warm) 45%, var(--orange-deep));
  }
  .holder {
    position: absolute;
    right: 33px;
    top: 240px;
    text-align: right;
    color: var(--white);
  }
  .holder__name { font-size: 15px; font-weight: 700; }
  .holder__role { font-size: 12px; margin-top: 2px; }

  .web {
    position: absolute;
    left: 0;
    width: 525px;
    top: 249px;
    text-align: center;
    font-size: 13px;
    letter-spacing: 0.6px;
  }
</style>
</head>
<body>
  <section class="card card--front">
    <div class="brand">
      <span class="brand__dot"></span>
      <span class="brand__name">PULSE MOTION</span>
      <span class="brand__sub">STUDIO</span>
    </div>
    <ul class="contact">
      <li>P : 305-555-0142</li>
      <li>E : dana@pulsemotionstudio.com</li>
      <li>W : www.Pulsemotionstudio.com</li>
    </ul>
    <div class="accent-area" role="img" aria-label="Decorative orange and yellow sweeping bands"></div>
    <div class="holder">
      <div class="holder__name">Dana Reyes</div>
      <div class="holder__role">Personal Fitness Trainer</div>
    </div>
  </section>

  <section class="card card--back">
    <div class="brand">
      <span class="brand__dot"></span>
      <span class="brand__name">PULSE MOTION</span>
      <span class="brand__sub">STUDIO</span>
    </div>
    <p class="web">www.Pulsemotionstudio.com</p>
  </section>
</body>
</html>
```